Creating a page for our Spanish tutoring service

We recently launched a new service and would like to create new "solutions" pages to add to our website.

Previously, we provided private one-on-one Spanish tutoring. Now, we are also providing group classes.

We have two documents with some basic copy on each offering. Our website is nice and does not require changes currently, but we do not have the internal bandwidth to build these pages. You would be using our existing design elements to build these two web pages.

Repurposing/copying blocks from our other pages is fine! We have a developer, so design only is required. If you do a good job on this first project, we will have many more pages and projects for you to do!

Our website is tutorlumo.com. TIA for any applicants.

---

Private classes copy:
https://files.quornbay.net/d/7kRtPw2mXa9vLq4ZsNe8Hb3uYc6Tf1Gd/view

Group classes copy:
https://files.quornbay.net/d/3pVxJh5nQe2WsKd8RmTa4YbLc9Uf7Zog/view

Target Market(s)

Online Spanish tutoring and online Spanish classes. We are a very high quality, yet affordable service. Our unique selling proposition is that we operate a completely remote team.

Current customers are typically well-to-do parents or professionals who want to learn Spanish for fun or personal development. They are usually in an okay standing financially (or want to be).

Those who pay for their kids to take lessons want them to have a better future or communicate with their families. Those who are young typically subscribe because they want a better future for themselves. Those who are 30+ years old learn for leisure, travel, or for ongoing professional development.

They want a quality product without paying the high costs associated with in-person tutoring, which is significantly more expensive. They also want to avoid cheaper solutions that are low cost but conversely low quality.

Number of Pages Required

2 page

Font styles to use
Other font styles liked:
• Avenir is our font

Requirements
Must have
• A look and feel consistent with the rest of our website.

```html
<!DOCTYPE html>
<html lang="en">
<head>
<meta charset="utf-8">
<title>TutorLumo – Group Spanish Classes Online</title>
<link rel="stylesheet" href="https://fonts.googleapis.com/css2?family=Nunito+Sans:wght@400;600;700;800&display=swap">
<style>
:root{
  --teal:#20b2a4;
  --teal-dark:#178f85;
  --teal-soft:#e6f6f4;
  --orange:#f68a3c;
  --ink:#2b3645;
  --muted:#6f7a88;
  --line:#e4e8ec;
  --red:#e4574e;
  --paper:#ffffff;
  --grey-bg:#f3f4f6;
  --footer-bg:#f6f6f3;
}
*{box-sizing:border-box;margin:0;padding:0}
html,body{width:1200px;height:2460px;overflow:hidden}
body{font-family:"Nunito Sans",Arial,sans-serif;color:var(--ink);background:var(--paper);position:relative}
.page{width:1200px;height:2460px;position:relative}

/* Hero */
.hero{position:relative;height:410px;overflow:hidden}
.hero-photo{position:absolute;inset:0;background:linear-gradient(100deg,#3f5f63 0%,#6f8d8f 35%,#b9c6c9 62%,#8a98a2 100%)}
.hero-shade{position:absolute;inset:0;background:linear-gradient(90deg,rgba(22,48,52,.72) 0%,rgba(22,48,52,.35) 45%,rgba(0,0,0,0) 70%)}
.nav{position:absolute;top:18px;left:100px;right:100px;display:flex;align-items:center;justify-content:space-between}
.brand{display:flex;align-items:center;gap:8px;font-weight:800;font-size:16px;color:#fff}
.brand-dot{width:14px;height:14px;border-radius:3px;background:var(--teal)}
.nav-links{display:flex;gap:34px;font-size:12px;font-weight:600;color:#fff;align-items:center}
.btn{display:inline-block;background:var(--orange);color:#fff;font-weight:700;border-radius:4px;text-align:center}
.nav .btn{font-size:11px;padding:8px 16px}
.hero-copy{position:absolute;left:100px;top:170px;width:380px;color:#fff}
.hero-copy h1{font-size:30px;line-height:36px;font-weight:800}
.hero-copy p{font-size:13px;line-height:19px;margin-top:12px;opacity:.9}
.hero-copy .btn{margin-top:26px;font-size:12px;padding:10px 22px}
.hero-rating{position:absolute;left:0;right:0;bottom:0;height:40px;background:rgba(20,36,40,.55);display:flex;align-items:center;justify-content:center;gap:10px;color:#fff;font-size:11px}
.stars{display:flex;gap:2px}
.stars span{width:11px;height:11px;background:var(--teal)}

/* Section titles */
.section-title{text-align:center;font-size:22px;font-weight:800;color:var(--ink)}

/* Why online */
.why{position:absolute;top:450px;left:0;right:0}
.features{display:flex;justify-content:center;gap:70px;margin-top:40px}
.feature{width:230px;text-align:center}
.feature svg{width:54px;height:54px}
.feature h3{font-size:15px;font-weight:800;margin-top:10px}
.feature p{font-size:11px;line-height:16px;color:var(--muted);margin-top:8px}
.divider{position:absolute;left:250px;right:250px;top:790px;height:1px;background:var(--line)}

/* Class types */
.kinds{position:absolute;top:850px;left:0;right:0}
.kinds .section-title{text-align:left;margin-left:250px}
.kinds-body{display:flex;margin:34px 0 0 250px;gap:50px}
.kind-list{width:320px}
.kind{display:flex;gap:14px;margin-bottom:34px}
.kind-num{flex:none;width:26px;height:26px;border-radius:50%;background:var(--teal);color:#fff;font-weight:800;font-size:13px;display:flex;align-items:center;justify-content:center}
.kind h3{font-size:16px;font-weight:800;color:var(--teal-dark)}
.kind p{font-size:11px;line-height:16px;color:var(--muted);margin-top:6px}
.kinds-art{width:360px;height:250px;border-radius:16px;background:radial-gradient(circle at 55% 50%,#fde6d6 0%,#e8f5f3 55%,#ffffff 80%)}

/* Comparison */
.compare{position:absolute;top:1200px;left:0;right:0}
.compare .sub{text-align:center;font-size:11px;color:var(--muted);width:460px;margin:10px auto 0;line-height:16px}
.table{width:700px;margin:30px auto 0;font-size:11px}
.row{display:grid;grid-template-columns:250px 150px 150px 150px;align-items:center;height:30px;border-bottom:1px solid var(--line)}
.row.head{font-weight:800;font-size:11px;height:34px}
.row .label{font-weight:600}
.row .cell{display:flex;justify-content:center}
.tick{width:16px;height:16px}
.cross{width:14px;height:14px}

/* Testimonials */
.testimonials{position:absolute;top:1720px;left:0;right:0;height:410px;background:var(--grey-bg);padding-top:34px}
.cards{display:flex;justify-content:center;gap:30px;margin-top:30px}
.card{width:210px}
.card-video{height:120px;border-radius:6px;position:relative;background:linear-gradient(135deg,#7b8fa1,#c9b7a8)}
.card:nth-child(2) .card-video{background:linear-gradient(135deg,#6b7fb8,#b7a4cc)}
.card:nth-child(3) .card-video{background:linear-gradient(135deg,#8aa0a0,#d6c2b4)}
.play{position:absolute;left:50%;top:50%;width:30px;height:30px;margin:-15px 0 0 -15px}
.card h4{font-size:12px;font-weight:800;margin-top:12px}
.card .role{font-size:10px;color:var(--muted)}
.card p{font-size:10.5px;line-height:15px;color:var(--muted);margin-top:8px}

/* Private tutoring band */
.private{position:absolute;top:2150px;left:190px;width:820px;height:72px;background:var(--teal);border-radius:4px;display:flex;align-items:center;justify-content:space-between;padding:0 30px;color:#fff}
.private h3{font-size:16px;font-weight:800}
.private p{font-size:10.5px;opacity:.9;margin-top:3px}
.private .btn{font-size:10.5px;padding:9px 16px}

/* Footer */
.footer{position:absolute;top:2250px;left:0;right:0;bottom:0;background:var(--footer-bg)}
.footer-cols{display:flex;gap:90px;padding:30px 0 0 100px}
.footer-col h5{font-size:12px;font-weight:800;margin-bottom:8px}
.footer-col a{display:block;font-size:10.5px;color:var(--muted);text-decoration:none;line-height:17px}
.social{display:flex;gap:6px;margin-top:4px}
.social span{width:16px;height:16px;border-radius:50%;background:var(--teal)}
.footer-bar{position:absolute;left:0;right:0;bottom:0;height:40px;border-top:1px solid var(--line);display:flex;align-items:center;justify-content:center;gap:10px;font-size:10px;color:var(--muted)}
.footer-bar .brand{color:var(--teal);font-size:12px}
</style>
</head>
<body>
<div class="page">

  <header class="hero">
    <div class="hero-photo" role="img" aria-label="Photo of a student on a laptop video call with a group Spanish class"></div>
    <div class="hero-shade"></div>
    <nav class="nav">
      <div class="brand"><span class="brand-dot"></span>TutorLumo</div>
      <div class="nav-links">
        <span>Private Tutoring</span><span>Group Classes</span><span>Kids Classes</span><span>Pricing</span><span>Blog</span>
        <span class="btn">Get a free trial</span>
      </div>
    </nav>
    <div class="hero-copy">
      <h1>Fun and effective group Spanish classes online</h1>
      <p>Practice Spanish conversation with native teachers in small groups, anytime, from anywhere.</p>
      <span class="btn">Try Free Now</span>
    </div>
    <div class="hero-rating">
      <span>Our students rate us</span><strong>Excellent</strong>
      <div class="stars"><span></span><span></span><span></span><span></span><span></span></div>
      <span>4.9 out of 5 on ReviewNest</span>
    </div>
  </header>

  <section class="why">
    <h2 class="section-title">Why online Spanish classes?</h2>
    <div class="features">
      <div class="feature">
        <svg viewBox="0 0 54 54" fill="none" stroke="#20b2a4" stroke-width="2.5"><rect x="6" y="8" width="42" height="28" rx="2"/><circle cx="18" cy="44" r="5"/><line x1="14" y1="20" x2="30" y2="20"/><line x1="14" y1="27" x2="38" y2="27"/></svg>
        <h3>Expert Teachers</h3>
        <p>Learn from certified native speakers trained to make every class clear, friendly and focused on real conversation.</p>
      </div>
      <div class="feature">
        <svg viewBox="0 0 54 54" fill="none" stroke="#20b2a4" stroke-width="2.5"><rect x="5" y="8" width="28" height="20" rx="3"/><rect x="21" y="24" width="28" height="20" rx="3"/><line x1="28" y1="33" x2="42" y2="33"/></svg>
        <h3>Engaging Lessons</h3>
        <p>Interactive topics, games and role plays keep you speaking and motivated from the first minute to the last.</p>
      </div>
      <div class="feature">
        <svg viewBox="0 0 54 54" fill="none" stroke="#20b2a4" stroke-width="3"><path d="M27 27c-5-7-9-10-14-10a10 10 0 0 0 0 20c5 0 9-3 14-10s9-10 14-10a10 10 0 0 1 0 20c-5 0-9-3-14-10z"/></svg>
        <h3>Unlimited Classes</h3>
        <p>Join as many group sessions as you like each week, at times that suit your schedule and time zone.</p>
      </div>
    </div>
  </section>
  <div class="divider"></div>

  <section class="kinds">
    <h2 class="section-title">What kinds of classes can you expect?</h2>
    <div class="kinds-body">
      <div class="kind-list">
        <div class="kind"><span class="kind-num">1</span><div><h3>Conversational</h3><p>Build confidence speaking about daily life, travel and work with guided conversation in small groups.</p></div></div>
        <div class="kind"><span class="kind-num">2</span><div><h3>Grammar</h3><p>Learn the rules that matter step by step, with clear examples and practice you can use straight away.</p></div></div>
      </div>
      <div class="kinds-art" role="img" aria-label="Illustration of students joining an online class on a large screen"></div>
    </div>
  </section>

  <section class="compare">
    <h2 class="section-title">Why TutorLumo?</h2>
    <p class="sub">See how our live classes compare with language apps and traditional schools.</p>
    <div class="table">
      <div class="row head"><span></span><span class="cell">TutorLumo</span><span class="cell">Language Apps</span><span class="cell">Language Schools</span></div>
      <div class="row"><span class="label">Unlimited &amp; Group classes</span><span class="cell"><svg class="tick" viewBox="0 0 16 16"><circle cx="8" cy="8" r="8" fill="#20b2a4"/><path d="M4.5 8.2l2.3 2.3 4.7-4.8" stroke="#fff" stroke-width="1.8" fill="none"/></svg></span><span class="cell"><svg class="cross" viewBox="0 0 14 14"><path d="M2 2l10 10M12 2L2 12" stroke="#e4574e" stroke-width="2.5"/></svg></span><span class="cell"><svg class="cross" viewBox="0 0 14 14"><path d="M2 2l10 10M12 2L2 12" stroke="#e4574e" stroke-width="2.5"/></svg></span></div>
      <div class="row"><span class="label">Native Speakers</span><span class="cell"><svg class="tick" viewBox="0 0 16 16"><circle cx="8" cy="8" r="8" fill="#20b2a4"/><path d="M4.5 8.2l2.3 2.3 4.7-4.8" stroke="#fff" stroke-width="1.8" fill="none"/></svg></span><span class="cell"><svg class="cross" viewBox="0 0 14 14"><path d="M2 2l10 10M12 2L2 12" stroke="#e4574e" stroke-width="2.5"/></svg></span><span class="cell"><svg class="cross" viewBox="0 0 14 14"><path d="M2 2l10 10M12 2L2 12" stroke="#e4574e" stroke-width="2.5"/></svg></span></div>
      <div class="row"><span class="label">Custom fresh lessons</span><span class="cell"><svg class="tick" viewBox="0 0 16 16"><circle cx="8" cy="8" r="8" fill="#20b2a4"/><path d="M4.5 8.2l2.3 2.3 4.7-4.8" stroke="#fff" stroke-width="1.8" fill="none"/></svg></span><span class="cell"><svg class="cross" viewBox="0 0 14 14"><path d="M2 2l10 10M12 2L2 12" stroke="#e4574e" stroke-width="2.5"/></svg></span><span class="cell"><svg class="cross" viewBox="0 0 14 14"><path d="M2 2l10 10M12 2L2 12" stroke="#e4574e" stroke-width="2.5"/></svg></span></div>
      <div class="row"><span class="label">Learn from anywhere</span><span class="cell"><svg class="tick" viewBox="0 0 16 16"><circle cx="8" cy="8" r="8" fill="#20b2a4"/><path d="M4.5 8.2l2.3 2.3 4.7-4.8" stroke="#fff" stroke-width="1.8" fill="none"/></svg></span><span class="cell"><svg class="tick" viewBox="0 0 16 16"><circle cx="8" cy="8" r="8" fill="#20b2a4"/><path d="M4.5 8.2l2.3 2.3 4.7-4.8" stroke="#fff" stroke-width="1.8" fill="none"/></svg></span><span class="cell"><svg class="cross" viewBox="0 0 14 14"><path d="M2 2l10 10M12 2L2 12" stroke="#e4574e" stroke-width="2.5"/></svg></span></div>
      <div class="row"><span class="label">Affordable to everyone</span><span class="cell"><svg class="tick" viewBox="0 0 16 16"><circle cx="8" cy="8" r="8" fill="#20b2a4"/><path d="M4.5 8.2l2.3 2.3 4.7-4.8" stroke="#fff" stroke-width="1.8" fill="none"/></svg></span><span class="cell"><svg class="tick" viewBox="0 0 16 16"><circle cx="8" cy="8" r="8" fill="#20b2a4"/><path d="M4.5 8.2l2.3 2.3 4.7-4.8" stroke="#fff" stroke-width="1.8" fill="none"/></svg></span><span class="cell"><svg class="cross" viewBox="0 0 14 14"><path d="M2 2l10 10M12 2L2 12" stroke="#e4574e" stroke-width="2.5"/></svg></span></div>
      <div class="row"><span class="label">Personalization</span><span class="cell"><svg class="tick" viewBox="0 0 16 16"><circle cx="8" cy="8" r="8" fill="#20b2a4"/><path d="M4.5 8.2l2.3 2.3 4.7-4.8" stroke="#fff" stroke-width="1.8" fill="none"/></svg></span><span class="cell"><svg class="tick" viewBox="0 0 16 16"><circle cx="8" cy="8" r="8" fill="#20b2a4"/><path d="M4.5 8.2l2.3 2.3 4.7-4.8" stroke="#fff" stroke-width="1.8" fill="none"/></svg></span><span class="cell"><svg class="tick" viewBox="0 0 16 16"><circle cx="8" cy="8" r="8" fill="#20b2a4"/><path d="M4.5 8.2l2.3 2.3 4.7-4.8" stroke="#fff" stroke-width="1.8" fill="none"/></svg></span></div>
      <div class="row"><span class="label">Grammar and vocabulary</span><span class="cell"><svg class="tick" viewBox="0 0 16 16"><circle cx="8" cy="8" r="8" fill="#20b2a4"/><path d="M4.5 8.2l2.3 2.3 4.7-4.8" stroke="#fff" stroke-width="1.8" fill="none"/></svg></span><span class="cell"><svg class="tick" viewBox="0 0 16 16"><circle cx="8" cy="8" r="8" fill="#20b2a4"/><path d="M4.5 8.2l2.3 2.3 4.7-4.8" stroke="#fff" stroke-width="1.8" fill="none"/></svg></span><span class="cell"><svg class="tick" viewBox="0 0 16 16"><circle cx="8" cy="8" r="8" fill="#20b2a4"/><path d="M4.5 8.2l2.3 2.3 4.7-4.8" stroke="#fff" stroke-width="1.8" fill="none"/></svg></span></div>
      <div class="row"><span class="label">Progress tracking</span><span class="cell"><svg class="tick" viewBox="0 0 16 16"><circle cx="8" cy="8" r="8" fill="#20b2a4"/><path d="M4.5 8.2l2.3 2.3 4.7-4.8" stroke="#fff" stroke-width="1.8" fill="none"/></svg></span><span class="cell"><svg class="tick" viewBox="0 0 16 16"><circle cx="8" cy="8" r="8" fill="#20b2a4"/><path d="M4.5 8.2l2.3 2.3 4.7-4.8" stroke="#fff" stroke-width="1.8" fill="none"/></svg></span><span class="cell"><svg class="tick" viewBox="0 0 16 16"><circle cx="8" cy="8" r="8" fill="#20b2a4"/><path d="M4.5 8.2l2.3 2.3 4.7-4.8" stroke="#fff" stroke-width="1.8" fill="none"/></svg></span></div>
      <div class="row"><span class="label">Engaging content</span><span class="cell"><svg class="tick" viewBox="0 0 16 16"><circle cx="8" cy="8" r="8" fill="#20b2a4"/><path d="M4.5 8.2l2.3 2.3 4.7-4.8" stroke="#fff" stroke-width="1.8" fill="none"/></svg></span><span class="cell"><svg class="tick" viewBox="0 0 16 16"><circle cx="8" cy="8" r="8" fill="#20b2a4"/><path d="M4.5 8.2l2.3 2.3 4.7-4.8" stroke="#fff" stroke-width="1.8" fill="none"/></svg></span><span class="cell"><svg class="tick" viewBox="0 0 16 16"><circle cx="8" cy="8" r="8" fill="#20b2a4"/><path d="M4.5 8.2l2.3 2.3 4.7-4.8" stroke="#fff" stroke-width="1.8" fill="none"/></svg></span></div>
    </div>
  </section>

  <section class="testimonials">
    <h2 class="section-title">What our students say</h2>
    <div class="cards">
      <article class="card">
        <div class="card-video" role="img" aria-label="Video testimonial thumbnail of a student"><svg class="play" viewBox="0 0 30 30"><circle cx="15" cy="15" r="15" fill="rgba(255,255,255,.85)"/><path d="M12 9l9 6-9 6z" fill="#20b2a4"/></svg></div>
        <h4>Irene Calder</h4><span class="role">Student since 2020</span>
        <p>The group classes are fun and relaxed. I finally speak Spanish with confidence when I travel, and the teachers are always patient.</p>
      </article>
      <article class="card">
        <div class="card-video" role="img" aria-label="Video testimonial thumbnail of a student"><svg class="play" viewBox="0 0 30 30"><circle cx="15" cy="15" r="15" fill="rgba(255,255,255,.85)"/><path d="M12 9l9 6-9 6z" fill="#20b2a4"/></svg></div>
        <h4>Owen Pratley</h4><span class="role">Professional learner</span>
        <p>I can join a class between meetings from anywhere. The lessons are practical and I notice real progress every single week.</p>
      </article>
      <article class="card">
        <div class="card-video" role="img" aria-label="Video testimonial thumbnail of a student"><svg class="play" viewBox="0 0 30 30"><circle cx="15" cy="15" r="15" fill="rgba(255,255,255,.85)"/><path d="M12 9l9 6-9 6z" fill="#20b2a4"/></svg></div>
        <h4>Nadia Fenwick</h4><span class="role">Parent of a student</span>
        <p>My kids love their teachers and look forward to class. It is great value and they now talk with their grandparents in Spanish.</p>
      </article>
    </div>
  </section>

  <section class="private">
    <div><h3>Private tutoring is also available</h3><p>Prefer one-on-one lessons? Learn at your own pace with a dedicated native tutor.</p></div>
    <span class="btn">LEARN MORE ABOUT PRIVATE TUTORING</span>
  </section>

  <footer class="footer">
    <div class="footer-cols">
      <div class="footer-col"><h5>Information</h5><a>About Us</a><a>Pricing</a><a>FAQ</a></div>
      <div class="footer-col"><h5>Services</h5><a>Private Tutoring</a><a>Group Classes</a><a>Kids Classes</a></div>
      <div class="footer-col"><h5>Company</h5><a>Careers</a><a>Teach with us</a><a>Blog</a></div>
      <div class="footer-col"><h5>Legal</h5><a>Privacy Policy</a><a>Terms of Use</a></div>
      <div class="footer-col"><h5>Get in touch</h5><a>hello@tutorlumo.com</a><div class="social"><span></span><span></span><span></span><span></span></div></div>
    </div>
    <div class="footer-bar"><span class="brand">TutorLumo</span><span>© 2024 TutorLumo. All rights reserved.</span></div>
  </footer>

</div>
</body>
</html>
```